Gedric's Lager BEER CAN

DESIGN USE
This is not for a business, it's for a (thoughtful) gift to my father. The design is going to be on a personalised beer can, so it will be a cylindrical shape. Basically, I'm giving him a few six-packs with his own beer label. I've attached the copy and put design specs below.
RATIONALE
My Dad is a cool guy, one of life’s absolute gems. He’s not a big drinker, but he likes a beer and he’s more likely to give them away at Christmas time than keep them in the fridge and drink them himself.
He’s also a master of Dad Jokes and offering pearls of wisdom, so combining a good beer with a funny Dad Joke or two on a can will be a great gift to give him for his birthday, Father’s Day or Christmas.
PLACEMENT
The front of the can needs to be my Dad’s head in cartoon form and GEDRIC’S LAGER has to be the most prominent wording.
While GEDRIC’S LAGER is the main heading…I’d like A TAMSWORTH RISE BREW up the top and GEDRIC’S LAGER IS LIFE’S BEER NECESSITY as the key wording wrapping around the bottom of the can.
I'd also like these sayings/jokes included (all of them OR as many that look cool and don't make the design too crowded):
“A beer in each hand is a balanced diet,” - Gedric

“This beer tastes like I’m not going to work tomorrow,” - Gedric

“Your beer isn’t half-full…it’s halfway to your next brew,” - Gedric

“My doc says I shouldn’t drink every day…that’s why I tend to drink at night,” - Gedric

“Two beer or not two beer,” - Shakesbeer

Why do frogs taste like beer?
Because of all the hops

What does Santa Claus drink?
A polar beer
Why do we like beer?
Coz you can’t drink bacon

Fat? Nah, beer makes you lean…
…against walls, doors…hotties

What's a beer’s favourite language?
Hebrew
DESIGN
Use the photos as a guide to turn my Dad (Gedric) into a cartoon - smiling/grinning, upbeat and happy. Not too old looking!
In terms of the can’s design, this is where I want YOU to be a design maestro. His head could burst through GEDRIC’S LAGER or simply have the lettering wrapped around his image.
Are the quotes and jokes in speech bubbles? Or are they in beer bubbles? Is a smaller version of Dad’s head used as a bullet point by each quote or joke?
FONT
Your choice! It just needs to be easy to read or and not too old-fashioned or - at the other extreme - too futuristic.
COLOUR
Your choice! He’s from a province that has red and black as their core colours, but if that doesn’t work, please go with a light teal/blue - or some other semi-masculine colour - and a dark colouring for the wording/lettering.
FORMAT
The approved copy needs to be provided as a PDF and a jpeg.
Maximum size is 250 MB
DIMENSIONS
160mm wide by 85mm high.

Target Market(s)

A target market of ONE - my Dad. I want him to LOVE his gift - his own personal beer can with his image and name on it.

Industry/Entity Type

Beer...

Colors

Designer to choose colors to be used in the design.

Requirements
Must have
• A fun, impactful BEER CAN design featuring my Dad's cartoon visage and some if not all of the Dad Jokes/beer sayings provided.

```html
<!DOCTYPE html>
<html lang="en">
<head>
<meta charset="utf-8">
<title>Gedric's Lager – Can Label</title>
<link rel="stylesheet" href="https://fonts.googleapis.com/css2?family=Cormorant+Garamond:wght@400&family=Pathway+Gothic+One&display=swap">
<style>
  :root {
    --page: #ffffff;
    --label-dark: #0b0b0b;
    --label-grain: #1c1c1c;
    --ink-light: #f3efe6;
    --cream: #f6ecd2;
    --amber: #d98a38;
    --ribbon-dark: #7a4c22;
    --ribbon-light: #d9a062;
    --ribbon-ink: #3a2412;
    --portrait-warm: #c8643a;
    --portrait-cool: #2b3550;
  }
  * { margin: 0; padding: 0; box-sizing: border-box; }
  html, body {
    width: 864px;
    height: 1200px;
    overflow: hidden;
    background: var(--page);
  }
  .canvas {
    position: relative;
    width: 864px;
    height: 1200px;
  }
  .label {
    position: absolute;
    left: 22px;
    top: 349px;
    width: 820px;
    height: 502px;
    overflow: hidden;
    background:
      repeating-linear-gradient(92deg, rgba(255,255,255,0.025) 0 2px, transparent 2px 9px),
      radial-gradient(ellipse at 50% 45%, var(--label-grain) 0%, var(--label-dark) 75%);
    color: var(--ink-light);
  }
  .label-kicker,
  .label-tagline {
    position: absolute;
    left: 0;
    width: 100%;
    text-align: center;
    font-family: "Cormorant Garamond", serif;
    font-weight: 400;
    color: var(--ink-light);
    letter-spacing: 0.5px;
    white-space: nowrap;
  }
  .label-kicker { top: 38px; font-size: 26px; }
  .label-tagline { top: 452px; font-size: 27px; }

  .quote-column,
  .joke-column {
    position: absolute;
    top: 100px;
    font-family: "Pathway Gothic One", sans-serif;
    font-size: 22px;
    line-height: 23px;
    white-space: nowrap;
  }
  .quote-column { left: 29px; width: 215px; }
  .joke-column { left: 631px; width: 180px; }
  .saying { margin-bottom: 7px; }
  .saying .attribution,
  .saying .punchline { color: var(--amber); }

  .portrait {
    position: absolute;
    left: 353px;
    top: 85px;
    width: 133px;
    height: 170px;
    border-radius: 62px 62px 20px 20px;
    background: linear-gradient(180deg, var(--portrait-warm) 0%, #a84d2c 55%, var(--portrait-cool) 100%);
  }
  .ribbon {
    position: absolute;
    left: 272px;
    top: 366px;
    width: 322px;
    height: 76px;
    border-radius: 6px;
    background: linear-gradient(90deg, var(--ribbon-dark) 0%, var(--ribbon-light) 50%, var(--ribbon-dark) 100%);
  }
  .brand-title {
    position: absolute;
    left: 254px;
    top: 232px;
    width: 344px;
    height: 126px;
    overflow: visible;
  }
  .brand-title text {
    font-family: "Pathway Gothic One", sans-serif;
    fill: var(--cream);
  }
  .brand-sub {
    position: absolute;
    left: 344px;
    top: 363px;
    width: 160px;
    text-align: center;
    font-family: "Pathway Gothic One", sans-serif;
    font-size: 46px;
    line-height: 50px;
    color: var(--ribbon-ink);
  }
</style>
</head>
<body>
<div class="canvas">
  <section class="label">
    <p class="label-kicker">A TAMSWORTH RISE BREW</p>

    <div class="quote-column">
      <p class="saying">“A beer in each hand is a<br>balanced diet,” <span class="attribution">- Gedric</span></p>
      <p class="saying">“This beer tastes like I’m not<br>going to work tomorrow,” -<br><span class="attribution">Gedric</span></p>
      <p class="saying">“Your beer isn’t<br>half-full…it’s halfway to your<br>next brew,” <span class="attribution">- Gedric</span></p>
      <p class="saying">“My doc says I shouldn’t<br>drink every day… that’s why I<br>tend to drink at night,” -<br><span class="attribution">Gedric</span></p>
      <p class="saying">“Two beer or not two beer,” -<br><span class="attribution">Shakesbeer</span></p>
    </div>

    <div class="portrait" role="img" aria-label="Cartoon portrait of Gedric smiling, wearing glasses and a blue checked shirt"></div>
    <svg class="brand-title" viewBox="0 0 344 126" aria-label="GEDRIC’S">
      <text x="0" y="122" font-size="168" textLength="344" lengthAdjust="spacingAndGlyphs">GEDRIC’S</text>
    </svg>
    <div class="ribbon" role="img" aria-label="Ornamental tan ribbon banner with flourishes"></div>
    <p class="brand-sub">LAGER</p>

    <div class="joke-column">
      <p class="saying">Why do frogs taste like<br>beer? <span class="punchline">Because of all the<br>hops</span></p>
      <p class="saying">What does Santa Claus<br>drink? <span class="punchline">A polar beer</span></p>
      <p class="saying">Why do we like beer?<br><span class="punchline">Coz you can’t drink<br>bacon</span></p>
      <p class="saying">Fat? Nah, beer makes<br>you lean… <span class="punchline">…against<br>walls, doors…hotties</span></p>
      <p class="saying">What's a beer’s favour-<br>ite language? <span class="punchline">Hebrew</span></p>
    </div>

    <p class="label-tagline">GEDRIC’S LAGER IS LIFE’S BEER NECESSITY</p>
  </section>
</div>
</body>
</html>
```